Just Sold Postcard

Real Estate/ Bramwell Oakes Realty.I'd like a template that I can use to change out the picture of the home, verbiage on the front, and address. I'm including a picture of what I've used in the past. I like designs that use red, with some blue and white. I'd like the ability to change the verbiage on the back as well.

Industry/Entity Type

Real Estate

Font styles to use
Serif
Sans Serif

```html
<!DOCTYPE html>
<html lang="en">
<head>
<meta charset="utf-8">
<title>Just Sold Postcard – Bramwell Oakes Realty</title>
<link href="https://fonts.googleapis.com/css2?family=Poppins:wght@400;500;600&family=Tinos&display=swap" rel="stylesheet">
<style>
  :root {
    --canvas: #ecebe8;
    --brand-blue: #1a4d9c;
    --brand-navy: #2a2f7a;
    --brand-red: #d3312f;
    --brand-red-soft: #e0574f;
    --orange-red: #ee4a32;
    --white: #ffffff;
    --rule: #c9c9c9;
    --ink: #222222;
    --photo-sky: #a9c7dc;
    --photo-lawn: #5f8a3a;
  }
  * { margin: 0; padding: 0; box-sizing: border-box; }
  html, body { width: 1200px; height: 1000px; overflow: hidden; }
  body {
    background: var(--canvas);
    font-family: "Poppins", Arial, sans-serif;
    position: relative;
  }
  .postcard {
    position: absolute;
    top: 109px;
    width: 403px;
    height: 312px;
    overflow: hidden;
    box-shadow: 0 2px 6px rgba(0,0,0,.25);
    background: var(--white);
  }
  .postcard-front { left: 155px; }
  .postcard-back { left: 628px; }
  .postcard svg.backdrop { position: absolute; inset: 0; }
  .abs { position: absolute; }

  /* Front */
  .listing-address {
    left: 268px; width: 130px; top: 32px;
    color: var(--white); font-weight: 500; font-size: 13px; line-height: 17px; text-align: center;
  }
  .listing-features {
    left: 272px; width: 128px; top: 78px;
    color: var(--white); font-size: 9.5px; line-height: 13.5px; text-align: center;
    white-space: nowrap;
  }
  .sold-badge {
    left: 255px; top: 150px; width: 105px; height: 33px;
    background: var(--white); border-radius: 5px; text-align: center;
    color: var(--brand-red); line-height: 13px; padding-top: 4px;
  }
  .sold-badge .sold-title { font-size: 11px; font-weight: 600; display: block; }
  .sold-badge .sold-sub { font-size: 11.5px; display: block; }
  .agent-block { left: 22px; top: 246px; color: var(--white); }
  .agent-block .agent-name { font-size: 18px; font-weight: 600; letter-spacing: .2px; line-height: 22px; }
  .agent-block .agent-line { font-size: 10.5px; line-height: 14px; }
  .brand-name {
    color: var(--brand-navy); font-weight: 600; white-space: nowrap;
  }
  .front-brand { left: 240px; width: 160px; top: 266px; font-size: 12.5px; text-align: center; }

  /* Back */
  .back-brand { left: 0; width: 195px; top: 33px; text-align: center; font-size: 14px; }
  .back-intro {
    left: 20px; width: 160px; top: 74px; text-align: center;
    font-size: 9.5px; line-height: 12px; color: var(--brand-navy);
  }
  .back-agent { left: 0; width: 195px; top: 122px; text-align: center; }
  .back-agent .agent-name { color: var(--orange-red); font-size: 18.5px; font-weight: 600; line-height: 22px; }
  .back-agent .agent-phone { color: var(--orange-red); font-size: 16px; line-height: 20px; }
  .back-agent .cta { color: var(--brand-navy); font-size: 13.5px; line-height: 16px; margin-top: 5px; }
  .back-agent .cta-sub { color: var(--brand-navy); font-size: 10.5px; line-height: 13px; }
  .back-agent .contact { color: var(--brand-navy); font-size: 10.5px; font-weight: 600; line-height: 13px; margin-top: 6px; }
  .divider { left: 194px; top: 16px; width: 1px; height: 242px; background: var(--rule); }
  .postage-box {
    left: 305px; top: 12px; width: 86px; height: 86px;
    border: 2px solid var(--rule);
    font-family: "Tinos", "Times New Roman", serif; font-size: 8.5px; line-height: 11px;
    text-align: center; color: var(--ink); padding-top: 20px;
  }
  .recipient {
    left: 228px; width: 144px; top: 143px; text-align: center; color: var(--ink);
  }
  .recipient .label { font-family: "Tinos", "Times New Roman", serif; font-size: 11px; margin-bottom: 10px; white-space: nowrap; }
  .recipient .lines { font-size: 9px; line-height: 11px; }
</style>
</head>
<body>

<section class="postcard postcard-front" aria-label="Postcard front">
  <svg class="backdrop" width="403" height="312" viewBox="0 0 403 312">
    <defs>
      <linearGradient id="photoTone" x1="0" y1="0" x2="0" y2="1">
        <stop offset="0" stop-color="var(--photo-sky)"/>
        <stop offset="0.55" stop-color="#8c8a7e"/>
        <stop offset="1" stop-color="var(--photo-lawn)"/>
      </linearGradient>
    </defs>
    <rect width="403" height="312" fill="var(--brand-blue)"/>
    <path d="M0,232 C120,238 280,215 403,172 L403,312 L0,312 Z" fill="var(--brand-red)"/>
    <path d="M150,312 C200,240 300,205 403,195 L403,312 Z" fill="var(--brand-red-soft)"/>
    <path d="M182,312 C230,258 320,230 403,222 L403,312 Z" fill="var(--white)"/>
    <path d="M0,0 L256,0 C270,40 274,112 246,164 C214,212 120,224 0,196 Z" fill="var(--white)"/>
    <path d="M0,0 L249,0 C263,40 266,110 240,159 C210,205 120,216 0,190 Z" fill="url(#photoTone)" role="img" aria-label="Photo of the sold home: two-storey stone and siding house with green lawn"/>
  </svg>

  <div class="abs listing-address">2716 Fernhill<br>Crest Drive</div>
  <div class="abs listing-features">Fabulous End Unit with<br>granite countertops<br>and hardwood floors.<br>Private lot</div>
  <div class="abs sold-badge"><span class="sold-title">JUST SOLD!</span><span class="sold-sub">Brought Buyer</span></div>
  <div class="abs agent-block">
    <div class="agent-name">DANA WHITFIELD</div>
    <div class="agent-line">Your Neighborhood Expert</div>
    <div class="agent-line">555.014.2290</div>
  </div>
  <div class="abs brand-name front-brand">Bramwell Oakes Realty</div>
</section>

<section class="postcard postcard-back" aria-label="Postcard back">
  <svg class="backdrop" width="403" height="312" viewBox="0 0 403 312">
    <defs>
      <linearGradient id="borderTone" x1="0" y1="0" x2="1" y2="1">
        <stop offset="0" stop-color="var(--orange-red)"/>
        <stop offset="1" stop-color="var(--brand-navy)"/>
      </linearGradient>
    </defs>
    <path d="M0,0 H403 V312 H0 Z M8,8 V304 H395 V8 Z" fill-rule="evenodd" fill="url(#borderTone)" opacity="0.85" role="img" aria-label="Red and blue airmail stripe border"/>
  </svg>

  <div class="abs brand-name back-brand">Bramwell Oakes Realty</div>
  <div class="abs back-intro">Lorem ipsum dolor sit amet, consectetur adipiscing elit. Integer nec blandit augue.</div>
  <div class="abs back-agent">
    <div class="agent-name">DANA WHITFIELD</div>
    <div class="agent-phone">(555)014-2290</div>
    <div class="cta">Contact me today!</div>
    <div class="cta-sub">For a FREE Market Analysis of<br>your home!</div>
    <div class="contact">555.014.2290 or<br>whitfield.dana@example.com</div>
  </div>
  <div class="abs divider"></div>
  <div class="abs postage-box">FIRST-CLASS MAIL<br>US. POSTAGE PAID<br>FAIRVIEW, ST<br>PERMIT NO. 27</div>
  <div class="abs recipient">
    <div class="label">RECIPIENT'S ADDRESS</div>
    <div class="lines">Lorem ipsum dolor sit amet,<br>consectetur adipiscing elit.<br>Integer nec blandit augue.</div>
  </div>
</section>

</body>
</html>
```